Simple AD for Digital Publication

Total Size 5" x 5", may include boarder or not
Image Provided; crop or use as background
Incorporate Logo and text as provided

Target Market(s)

Sound Contractors / Integrators

Industry/Entity Type

Audio Video Lighting

Requirements
Must have
• Bold Look that reflects our brand. see website: tovermundic.com - cohesive text and style

```html
<!DOCTYPE html>
<html lang="en">
<head>
<meta charset="utf-8">
<title>Protect &amp; Conceal – Tovermund Stage Co</title>
<link rel="stylesheet" href="https://fonts.googleapis.com/css2?family=Open+Sans:ital,wght@0,400;0,700;0,800;1,700&display=swap">
<style>
  :root {
    --brand-red: #ac1f27;
    --ink: #111111;
    --slate: #4a4b4d;
    --paper: #ffffff;
  }
  * { margin: 0; padding: 0; box-sizing: border-box; }
  html, body { width: 1200px; height: 1200px; overflow: hidden; background: var(--paper); }
  .ad {
    position: relative;
    width: 1200px;
    height: 1200px;
    background: var(--paper);
    font-family: "Open Sans", Arial, sans-serif;
    overflow: hidden;
  }
  .header-band {
    position: absolute;
    left: 0; top: 0;
    width: 1200px; height: 339px;
    background: var(--brand-red);
  }
  .headline {
    position: absolute;
    left: 0; top: 30px;
    width: 1200px;
    text-align: center;
    color: var(--paper);
    font-weight: 800;
    font-size: 108px;
    line-height: 1;
    letter-spacing: -1px;
  }
  .headline .amp { font-weight: 400; font-size: 72px; vertical-align: 10px; }
  .subheadline {
    position: absolute;
    left: 0; top: 172px;
    width: 1200px;
    text-align: center;
    color: var(--paper);
    font-weight: 700;
    font-size: 45px;
    line-height: 1;
  }
  .hero-photo {
    position: absolute;
    left: 94px; top: 242px;
    width: 1012px; height: 756px;
    background:
      radial-gradient(ellipse 60% 18% at 50% 45%, rgba(255,214,140,0.45), transparent 70%),
      linear-gradient(180deg, #2b2a3d 0%, #3a3346 22%, #2f4a2c 40%, #3d5a2e 50%, #9c8a7c 62%, #b9a79c 80%, #a08c80 100%);
  }
  .brand {
    position: absolute;
    left: 128px; top: 1050px;
    display: flex;
    align-items: center;
    gap: 22px;
  }
  .brand-square {
    width: 70px; height: 70px;
    background: var(--slate);
  }
  .brand-name {
    font-weight: 800;
    font-size: 62px;
    line-height: 1;
    color: var(--slate);
    letter-spacing: -1px;
  }
  .dealer-button {
    position: absolute;
    left: 961px; top: 1000px;
    width: 211px; height: 139px;
    background: var(--ink);
    border-radius: 0 0 0 90px;
    color: var(--paper);
    text-align: center;
  }
  .dealer-button .label {
    display: block;
    margin-top: 10px;
    font-weight: 700;
    font-size: 22px;
    letter-spacing: -0.3px;
  }
  .dealer-button .icon-slot {
    display: block;
    width: 92px; height: 50px;
    margin: 14px auto 0;
    background: var(--paper);
    border-radius: 8px;
  }
  .click-note {
    position: absolute;
    left: 961px; top: 1146px;
    width: 211px;
    text-align: center;
    font-weight: 700;
    font-style: italic;
    font-size: 20px;
    color: var(--ink);
  }
</style>
</head>
<body>
  <main class="ad">
    <div class="header-band"></div>
    <h1 class="headline">Protect <span class="amp">&amp;</span> Conceal</h1>
    <p class="subheadline">High and Low Voltage Connectivity</p>

    <div class="hero-photo" role="img" aria-label="Photo of a recessed black stage floor pocket on a wooden stage with cables running out of it, a lit evergreen garland behind, and rows of blue church pews in the background"></div>

    <div class="brand">
      <span class="brand-square"></span>
      <span class="brand-name">TOVERMUND STAGE CO</span>
    </div>

    <div class="dealer-button">
      <span class="label">Become a Dealer</span>
      <span class="icon-slot" role="img" aria-label="Handshake icon"></span>
    </div>
    <p class="click-note">(click here)</p>
  </main>
</body>
</html>
```